Letterhead for SaaS

Design a letterhead that aligns with our new business card, using our logo and color scheme and text defined in the Branding Guide to ensure consistency. Consider incorporating a subtle watermark for added elegance. The layout should reflect the card's style, creating a cohesive look across our stationery.

```html
<!DOCTYPE html>
<html lang="en">
<head>
<meta charset="utf-8">
<title>Veltris Letterhead</title>
<link href="https://fonts.googleapis.com/css2?family=Montserrat:wght@500;600;800&display=swap" rel="stylesheet">
<style>
  :root {
    --navy: #111a2c;
    --navy-deep: #0b111d;
    --navy-light: #1d2a45;
    --cyan: #14b1e3;
    --wolf-blue: #2b4b9b;
    --white: #ffffff;
    --watermark: #ececec;
    --page-bg: #ffffff;
  }
  * { margin: 0; padding: 0; box-sizing: border-box; }
  html, body {
    width: 1200px;
    height: 1005px;
    overflow: hidden;
    background: var(--page-bg);
    font-family: "Montserrat", sans-serif;
  }
  .canvas { position: relative; width: 1200px; height: 1005px; }

  .sheet {
    position: absolute;
    top: 100px;
    width: 566px;
    height: 731px;
    overflow: hidden;
  }
  .sheet-front { left: 9px; background: var(--white); }
  .sheet-back {
    left: 621px;
    background: radial-gradient(ellipse at 45% 40%, var(--navy-light) 0%, var(--navy) 45%, var(--navy-deep) 100%);
  }

  .header-band {
    position: absolute;
    left: 0; top: 0;
    width: 100%;
    height: 119px;
    background: linear-gradient(120deg, var(--navy-light) 0%, var(--navy) 40%, var(--navy-deep) 70%, var(--navy) 100%);
    overflow: hidden;
  }
  .brand-badge {
    position: absolute;
    left: 23px;
    top: 14px;
    width: 182px;
    height: 182px;
    border-radius: 50%;
    background: var(--white);
  }
  .brand-name {
    position: absolute;
    left: 23px;
    top: 76px;
    width: 182px;
    text-align: center;
    font-weight: 800;
    font-size: 25px;
    letter-spacing: 1px;
    color: var(--navy);
  }

  .contact-list {
    position: absolute;
    left: 325px;
    top: 38px;
    list-style: none;
  }
  .contact-item {
    display: flex;
    align-items: center;
    gap: 6px;
    height: 23px;
    color: var(--white);
    font-weight: 500;
    font-size: 14px;
  }
  .contact-item.web { letter-spacing: 2px; font-size: 15px; }
  .contact-icon {
    width: 20px; height: 20px;
    border-radius: 50%;
    background: var(--cyan);
    display: flex; align-items: center; justify-content: center;
    flex: none;
  }

  .watermark {
    position: absolute;
    left: 0; top: 355px;
    width: 100%;
    text-align: center;
    font-weight: 800;
    font-size: 64px;
    letter-spacing: 4px;
    color: var(--watermark);
  }

  .footer-band {
    position: absolute;
    left: 0; bottom: 0;
    width: 566px; height: 22px;
  }

  .background-pattern {
    position: absolute; inset: 0;
  }
  .back-mark {
    position: absolute;
    left: 0; top: 335px;
    width: 100%;
    text-align: center;
    font-weight: 800;
    font-size: 64px;
    letter-spacing: 4px;
    color: var(--wolf-blue);
  }
</style>
</head>
<body>
<div class="canvas">

  <section class="sheet sheet-front" aria-label="Letterhead front">
    <header class="header-band">
      <div class="brand-badge"></div>
      <div class="brand-name">VELTRIS</div>
      <ul class="contact-list">
        <li class="contact-item web">
          <span class="contact-icon">
            <svg width="12" height="12" viewBox="0 0 12 12" fill="none" stroke="#fff" stroke-width="1"><circle cx="6" cy="6" r="5"/><ellipse cx="6" cy="6" rx="2.2" ry="5"/><line x1="1" y1="6" x2="11" y2="6"/></svg>
          </span>
          WWW.VELTRIS.COM
        </li>
        <li class="contact-item">
          <span class="contact-icon">
            <svg width="12" height="10" viewBox="0 0 12 10" fill="none" stroke="#fff" stroke-width="1.2"><rect x="1" y="1" width="10" height="8" rx="1"/><polyline points="1,2 6,6 11,2"/></svg>
          </span>
          jordan.m@veltris.com
        </li>
        <li class="contact-item">
          <span class="contact-icon">
            <svg width="11" height="11" viewBox="0 0 24 24" fill="#fff"><path d="M6.6 10.8a15.1 15.1 0 0 0 6.6 6.6l2.2-2.2a1 1 0 0 1 1-.25 11.4 11.4 0 0 0 3.6.57 1 1 0 0 1 1 1V20a1 1 0 0 1-1 1A17 17 0 0 1 3 4a1 1 0 0 1 1-1h3.5a1 1 0 0 1 1 1c0 1.25.2 2.45.57 3.57a1 1 0 0 1-.25 1z"/></svg>
          </span>
          (555) 014-2290
        </li>
      </ul>
    </header>

    <div class="watermark">VELTRIS</div>

    <svg class="footer-band" viewBox="0 0 566 22" preserveAspectRatio="none">
      <defs>
        <linearGradient id="footerNavy" x1="0" x2="1">
          <stop offset="0" stop-color="#1d2a45"/>
          <stop offset="1" stop-color="#0b111d"/>
        </linearGradient>
      </defs>
      <polygon points="0,0 299,0 285,22 0,22" fill="url(#footerNavy)"/>
      <polygon points="325,0 566,0 566,22 307,22" fill="var(--cyan)"/>
    </svg>
  </section>

  <section class="sheet sheet-back" aria-label="Letterhead back">
    <div class="background-pattern" role="img" aria-label="Dark navy faceted polygon background pattern"></div>
    <div class="back-mark">VELTRIS</div>
  </section>

</div>
</body>
</html>
```